Granite Path Fitness Presents Harbor Touch Massage with Marguerite

I'm promoting my massage therapy business which is located in a personal one on one training gym. A few of the modalities I offer are:
Basic Relaxation -light or deep.
Medical Massage- specific work for a specific problem.
Reflexology- feet feet and more feet.
Thai Yoga- I stretch you.
Scalp and Feet- Mega tension relief.
For more details, information and to make an appointment call Marguerite at :731 528 4170. E mail: tulipbaker@mailvex.com
I was playing with this: Bring me your tired, aching, stressed-out body and give me a chance to work some magic. (I hate promoting myself and that was extreme for me.)

Target Market(s)

Gym members and walk-ins from the Uptown Kingston, NY neighborhood.

Industry/Entity Type

Business

Colors

Designer to choose colors to be used in the design.

Requirements
Must have
• My name and phone # and my e mail address.
Should not have
• Anything sexual. This is serious healing work done by a licenced professional so there can be no confusion as to intent.

```html
<!DOCTYPE html>
<html lang="en">
<head>
<meta charset="utf-8">
<title>Massage Therapy at Granite Path Fitness</title>
<link rel="stylesheet" href="https://fonts.googleapis.com/css2?family=PT+Sans:wght@400;700&family=Poppins:ital,wght@0,300;0,500;1,300&display=swap">
<style>
  :root {
    --teal: #3cc0cc;
    --teal-soft: #d7f1f4;
    --grey-title: #a6a8ab;
    --grey-text: #9a9c9f;
    --ink: #1d1d1f;
    --body: #444648;
    --paper: #ffffff;
    --skin-light: #f3ddcf;
    --skin-mid: #e8c3ad;
  }
  * { margin: 0; padding: 0; box-sizing: border-box; }
  html, body { width: 1200px; height: 800px; overflow: hidden; background: var(--paper); }
  .flyer { position: relative; width: 1200px; height: 800px; background: var(--paper); overflow: hidden; font-family: "Poppins", sans-serif; }

  .hand-photo {
    position: absolute; left: 0; top: 520px; width: 960px; height: 280px;
    background: radial-gradient(ellipse 60% 45% at 55% 45%, var(--skin-mid) 0%, var(--skin-light) 45%, rgba(255,255,255,0) 100%);
  }

  .headline { position: absolute; left: 50px; top: 72px; }
  .headline__title { font-family: "PT Sans", sans-serif; font-weight: 700; font-size: 54px; line-height: 54px; color: var(--grey-title); letter-spacing: 1px; }
  .headline__venue { font-family: "PT Sans", sans-serif; font-weight: 700; font-size: 24px; color: var(--teal); margin-top: 10px; letter-spacing: 0.3px; }

  .service-icon {
    position: absolute; width: 140px; height: 140px; border-radius: 50%;
    border: 4px solid var(--teal); background: var(--paper);
    display: flex; align-items: center; justify-content: center;
  }
  .service-icon__fill { width: 104px; height: 104px; border-radius: 50%; background: var(--teal-soft); }

  .service { position: absolute; }
  .service__name { font-weight: 500; font-size: 21px; color: var(--ink); line-height: 28px; }
  .service__note { font-weight: 300; font-style: italic; font-size: 21px; color: var(--teal); line-height: 28px; }

  .bubble {
    position: absolute; left: 428px; top: 190px; width: 424px; height: 410px; border-radius: 50%;
    background: radial-gradient(circle at 50% 40%, rgba(255,255,255,1) 55%, rgba(232,238,240,0.9) 85%, rgba(214,222,226,0.7) 100%);
    box-shadow: 0 6px 24px rgba(0,0,0,0.06);
  }
  .pitch {
    position: absolute; left: 428px; top: 255px; width: 424px; text-align: center;
    font-family: "PT Sans", sans-serif; font-weight: 700; font-size: 36px; line-height: 42px;
  }
  .pitch__ask { color: var(--grey-text); }
  .pitch__promise { color: var(--teal); }

  .contact { position: absolute; left: 490px; top: 690px; color: var(--body); font-weight: 300; }
  .contact__lead { font-size: 19px; }
  .contact__row { display: flex; align-items: center; margin-top: 12px; font-size: 21px; }
  .contact__item { display: flex; align-items: center; margin-right: 30px; }
  .contact__item svg { width: 26px; height: 26px; margin-right: 10px; }
  .contact__name { color: var(--teal); font-style: italic; margin-left: 6px; }
</style>
</head>
<body>
<main class="flyer">
  <div class="hand-photo" role="img" aria-label="Photo of an open hand, palm up, holding the message bubble"></div>

  <header class="headline">
    <h1 class="headline__title">MASSAGE<br>THERAPY</h1>
    <p class="headline__venue">AT GRANITE PATH FITNESS</p>
  </header>

  <div class="service-icon" style="left:353px; top:65px;"><div class="service-icon__fill" role="img" aria-label="Icon of a person seated in meditation"></div></div>
  <div class="service" style="left:515px; top:92px;">
    <p class="service__name">Basic Relaxation</p>
    <p class="service__note">- light or deep</p>
  </div>

  <div class="service-icon" style="left:734px; top:67px;"><div class="service-icon__fill" role="img" aria-label="Icon of a therapist massaging a client on a table"></div></div>
  <div class="service" style="left:902px; top:100px;">
    <p class="service__name">Medical Massage</p>
    <p class="service__note">- specific work<br>for a specific<br>problem</p>
  </div>

  <div class="service-icon" style="left:67px; top:245px;"><div class="service-icon__fill" role="img" aria-label="Icon of hands working on a foot"></div></div>
  <div class="service" style="left:232px; top:272px;">
    <p class="service__name">Reflexology</p>
    <p class="service__note">- feet feet<br>and more<br>feet</p>
  </div>

  <div class="service-icon" style="left:79px; top:427px;"><div class="service-icon__fill" role="img" aria-label="Icon of a Thai yoga stretch"></div></div>
  <div class="service" style="left:244px; top:478px;">
    <p class="service__name">Thai Yoga</p>
    <p class="service__note">- I stretch you</p>
  </div>

  <div class="service-icon" style="left:918px; top:255px;"><div class="service-icon__fill" role="img" aria-label="Icon of hands massaging a scalp"></div></div>
  <div class="service" style="left:880px; top:412px; text-align:right; width:260px;">
    <p class="service__name" style="text-align:center;">Scalp and Feet</p>
    <p class="service__note">- mega tension relief</p>
  </div>

  <div class="bubble"></div>
  <p class="pitch">
    <span class="pitch__ask">BRING ME<br>YOUR TIRED,<br>ACHING,<br>STRESSED-OUT BODY</span><br>
    <span class="pitch__promise">AND GIVE ME A<br>CHANCE TO WORK<br>SOME MAGIC.</span>
  </p>

  <footer class="contact">
    <p class="contact__lead">For more details, information and to make an appointment :</p>
    <div class="contact__row">
      <span class="contact__item">
        <svg viewBox="0 0 26 26" aria-hidden="true"><circle cx="13" cy="13" r="13" fill="var(--teal)"/><path d="M9 6.5c.8-.4 1.6 0 2 .8l1 2c.3.7.1 1.4-.5 1.8l-.8.5c.6 1.6 1.8 2.9 3.4 3.6l.6-.8c.4-.6 1.2-.8 1.8-.4l1.9 1.1c.7.4 1 1.3.6 2l-.6 1c-.6.9-1.7 1.3-2.7 1-4-1.3-7-4.4-8.1-8.4-.3-1 .1-2 1-2.6z" fill="#fff"/></svg>
        731 528 4170<span class="contact__name">Marguerite</span>
      </span>
      <span class="contact__item">
        <svg viewBox="0 0 26 26" aria-hidden="true"><circle cx="13" cy="13" r="13" fill="var(--teal)"/><rect x="6.5" y="8.5" width="13" height="9" rx="1" fill="#fff"/><path d="M7 9l6 5 6-5" fill="none" stroke="var(--teal)" stroke-width="1.4"/></svg>
        tulipbaker<span style="color:var(--teal)">@</span>mailvex.com
      </span>
    </div>
  </footer>
</main>
</body>
</html>
```